Bold, Captivating, Passion driven brochure design for an Inspirational Speaker and Trainer

I am looking for a brochure design that will immediately draw people into my energy field. It needs to have bold colors yet soft on the eyes. Placement of information is key. I am a Success Navigator and Inspirational Speaker in need of a brochure design that brings who I am and the value I offer to life... needs to jump right off the page.

Target Market(s)

Small business owners and savvy professionals ages 25-45. I am mainly geared towards the beauty industry because that's where I started; however, I want my materials to help me branch out more beyond the beauty industry.

Contact Information for Business Card

Marcus T. Hale, LLC
Marcus T. Hale
Success Navigator & Inspirational Speaker

Font styles to use
Serif

Requirements
Must have
• Cobalt blue is my favorite color... I would like blues of some kind peppered into the color scheme. Needs to look upscale and seasoned in what I do/offer. Serious and yet inviting - not playful but also not too rigid. Essentially, I don't take myself seriously; however, I take what i do very seriously.
Should not have
• Must not look overdone or inauthentic; not traditional and not overly modernized either

```html
<!DOCTYPE html>
<html lang="en">
<head>
<meta charset="utf-8">
<title>Marcus T. Hale — Brochure</title>
<link rel="stylesheet" href="https://fonts.googleapis.com/css2?family=Roboto:wght@300;400;700&display=swap">
<style>
  :root {
    --cobalt: #155d93;
    --cobalt-deep: #0f4f80;
    --sky: #1c9ad8;
    --paper: #ffffff;
    --mist: #e9edf1;
    --label: #dde2e7;
    --label-text: #17568a;
    --ground: #d9dde2;
    --photo-light: #e4e6e9;
    --photo-dark: #4a4f57;
  }
  * { box-sizing: border-box; margin: 0; padding: 0; }
  html, body { width: 1200px; height: 900px; overflow: hidden; }
  body { background: var(--ground); font-family: "Roboto", Arial, sans-serif; color: var(--paper); }

  .brochure {
    position: absolute; left: 30px; top: 20px;
    width: 1140px; height: 860px;
    display: flex;
    box-shadow: 0 6px 24px rgba(0,0,0,.18);
  }
  .panel { position: relative; width: 380px; height: 860px; background: var(--cobalt); overflow: hidden; }
  .panel + .panel { border-left: 1px solid rgba(0,0,0,.12); }
  .panel-art { position: absolute; inset: 0; }

  .label {
    display: inline-block; background: var(--label); color: var(--label-text);
    font-weight: 700; font-size: 15px; padding: 6px 14px;
    box-shadow: 0 2px 4px rgba(0,0,0,.2);
  }
  .copy { font-weight: 300; font-size: 13.5px; line-height: 1.45; }
  .copy p + p { margin-top: 12px; }

  /* panel one */
  .difference { position: absolute; left: 52px; top: 48px; width: 280px; }
  .difference .label { margin-bottom: 16px; }
  .contact { position: absolute; left: 52px; top: 380px; width: 280px; }
  .contact .label { margin-bottom: 14px; }
  .contact-list { list-style: none; font-weight: 300; font-size: 13.5px; line-height: 1.5; }

  /* panel two */
  .about { position: absolute; left: 48px; top: 420px; width: 290px; }
  .about .label { margin-bottom: 22px; }
  .about .copy { font-size: 15px; line-height: 1.45; text-align: center; }

  /* panel three */
  .name-lockup { position: absolute; left: 96px; top: 392px; display: flex; align-items: center; gap: 10px; }
  .name-lockup .mark { width: 26px; height: 26px; background: var(--paper); }
  .name-lockup .name {
    background: var(--sky); color: var(--paper); font-weight: 400;
    font-size: 17px; letter-spacing: .5px; padding: 6px 16px;
  }
  .headline { position: absolute; left: 34px; top: 490px; font-weight: 400; font-size: 27px; line-height: 1.25; text-transform: uppercase; }
  .headline .cap { font-size: 36px; font-weight: 700; }
  .tagline { position: absolute; left: 0; right: 0; top: 640px; text-align: center; font-weight: 300; font-size: 19px; }
</style>
</head>
<body>
<main class="brochure">

  <!-- panel one: difference & contact -->
  <section class="panel panel-difference">
    <svg class="panel-art" width="380" height="860" viewBox="0 0 380 860">
      <defs>
        <clipPath id="portrait-casual-clip"><circle cx="150" cy="700" r="112"/></clipPath>
        <radialGradient id="portrait-casual-fill" cx="50%" cy="55%" r="60%">
          <stop offset="0" stop-color="var(--photo-dark)"/>
          <stop offset=".55" stop-color="#8c8f95"/>
          <stop offset="1" stop-color="var(--photo-light)"/>
        </radialGradient>
      </defs>
      <circle cx="150" cy="700" r="138" fill="var(--paper)"/>
      <path d="M150 562 A138 138 0 0 1 288 700 A138 138 0 0 1 150 838" fill="none" stroke="var(--sky)" stroke-width="14"/>
      <g clip-path="url(#portrait-casual-clip)" role="img" aria-label="Portrait of Marcus T. Hale in a casual shirt">
        <rect x="30" y="580" width="240" height="240" fill="url(#portrait-casual-fill)"/>
      </g>
    </svg>

    <div class="difference">
      <span class="label">Our Difference</span>
      <div class="copy">
        <p>Marcus T. Hale, LLC is dedicated to one single goal for your innovative business – producing permanent cures for all your business pains.</p>
        <p>Rather than treating the symptoms, we go beyond the surface to help you discover the root causes of your top challenges. We then work with you to craft customized Business Solutions tailored to your specific needs allowing you to thrive in any economic climate.</p>
        <p>Essentially, we are the difference that makes the DIFFERENCE in helping you make your business recession-proof.</p>
      </div>
    </div>

    <div class="contact">
      <span class="label">Contact Us</span>
      <ul class="contact-list">
        <li>P.O. Box 418</li>
        <li>Harbor View, NJ 07100-2418</li>
        <li>Office: 555.201.4470</li>
        <li>Mobile: 555.201.8832</li>
        <li>Email: marcus@marcusthale.com</li>
        <li>Website: http://www.marcusthale.com</li>
      </ul>
    </div>
  </section>

  <!-- panel two: about -->
  <section class="panel panel-about">
    <svg class="panel-art" width="380" height="860" viewBox="0 0 380 860">
      <defs>
        <linearGradient id="portrait-action-fill" x1="0" y1="0" x2="1" y2="1">
          <stop offset="0" stop-color="var(--photo-light)"/>
          <stop offset=".6" stop-color="#9a9ca1"/>
          <stop offset="1" stop-color="#3c4048"/>
        </linearGradient>
      </defs>
      <path d="M0 0 H380 V330 C250 330 80 300 0 210 Z" fill="var(--mist)"/>
      <path d="M0 0 C0 140 60 260 200 320 C110 250 60 150 70 0 Z" fill="var(--sky)"/>
      <path d="M70 0 C60 150 110 250 200 320 C270 345 340 345 380 335 V0 Z" fill="var(--paper)"/>
      <rect x="150" y="40" width="230" height="260" fill="url(#portrait-action-fill)" role="img" aria-label="Photo of Marcus T. Hale in a suit raising a fist"/>
    </svg>

    <div class="about">
      <span class="label">About me</span>
      <div class="copy">
        <p>Marcus T. Hale is a Success Navigator committed to helping you discover and unleash your remarkable untapped potential.</p>
        <p>His simple system has helped thousands of innovative business owners achieve the milestones that matter most allowing them to thrive in any economic climate.</p>
        <p>Marcus has been helping others achieve amazing breakthrough results for more than 15 years.</p>
      </div>
    </div>
  </section>

  <!-- panel three: cover -->
  <section class="panel panel-cover">
    <svg class="panel-art" width="380" height="860" viewBox="0 0 380 860">
      <defs>
        <clipPath id="portrait-cover-clip"><circle cx="200" cy="235" r="140"/></clipPath>
        <radialGradient id="portrait-cover-fill" cx="50%" cy="60%" r="60%">
          <stop offset="0" stop-color="#2c3e5c"/>
          <stop offset=".5" stop-color="#7f8794"/>
          <stop offset="1" stop-color="var(--photo-light)"/>
        </radialGradient>
      </defs>
      <path d="M0 0 H380 V300 C300 380 160 400 0 360 Z" fill="var(--paper)"/>
      <path d="M0 0 H120 C40 60 0 150 0 250 Z" fill="var(--mist)"/>
      <circle cx="200" cy="235" r="168" fill="var(--paper)"/>
      <path d="M60 180 A150 150 0 0 1 340 150" fill="none" stroke="var(--sky)" stroke-width="16"/>
      <path d="M345 260 A150 150 0 0 1 120 370" fill="none" stroke="var(--sky)" stroke-width="16"/>
      <g clip-path="url(#portrait-cover-clip)" role="img" aria-label="Portrait of Marcus T. Hale smiling in a blazer">
        <rect x="60" y="95" width="280" height="280" fill="url(#portrait-cover-fill)"/>
      </g>
    </svg>

    <div class="name-lockup">
      <span class="mark"></span>
      <span class="name">MARCUS T. HALE</span>
    </div>

    <h1 class="headline">
      <span class="cap">U</span>nleash <span class="cap">Y</span>our<br>
      <span class="cap">U</span>ntapped <span class="cap">P</span>otential
    </h1>
    <p class="tagline">Live Life by Your Design</p>
  </section>

</main>
</body>
</html>
```